flat health bread wrap

PREFERENCE WILL BE GIVEN TO DESIGNERS WHO CAN SUBMIT THEIR INITIAL IDEAS PRIOR TO 9.00AM FRIDAY 12TH AUGUST 2010 MELBOURNE AUSTRALIA TIME!

additonal packaging information

target market:

mothers who make their childrens lunch, people looking for a healthy alternative and a change to normal bread,

pack size

34cm length X 28.5cm width
crystal-clear, see through plastic re-sealable zip lock pack.

brand name: tidy fold
product explanation: mediterranean flat bread
product features: see below
raw product size: 22cm X 22cm SQUARE
most US products of this style are round or oval! ours will be new to the US market.
colour: pale pita bread colour
markings on bread: pale fried hotplate markings
number of pieces per pack: 8
gross weight of product 250 grams
product manufactured in melbourne australia
accreditations: kosher and halal

front of pack: good design and accreditations (KOSHER AND HALAL)

back of pack: barcode, how to wrap instructions,
US nutritional panel, ingredient list (flour, water, salt and vitamins. gluten allegen warning. oxygen absorbing sachet warning (do not eat)
company address and contact details,

3 flavours: Rye, White, wholmeal and Corn.

marketing
new product designed specificaly for the US market,
distribution: supermarkets, health food stores
retail price: USD $2.99

# New Middle Eastern style Healthy Valley Loaf Wraps. (Tortillas)
# Square flat bread sheets
# For distribution across USA
# Targetting
* Health food enthusiats
* New Age consumers
* Mothers looking for lunchbox options
* Those seeking a substitute for the traditional lunch sandwich
* These square flat bread sheets replace the traditional bread made sandwich

These products are:
# Shelf stable (minimum 6 months) without refrigeration
# Completely free of:
- preservatives
- colours
- yeast
- cholesterol
- trans fats
- hydrogenated oils
# soft and pliable, and extremely thin
# made from wheat/rye/corn flour, water and salt AND NOTHING ELSE
# organic and other options available
# manufactured in Melbourne Australia
# Kosher and Halal certified

Our proposed brand name is TIDY FOLD
# we prefer to dwell on the humourous perspectives of the name
# our product will look something like these - http://www.valleyloaf.com.au/cgi-bin/index.pl?menu_id=3
and these http://www.sunridgeovens.com.au/tavi.html

# This range is unique
in that it is without additives preservatives etc
is NOT round but square in shape
^ we wouold like to emphasise this
^ packaged in transparent zip-lock bags

Reason: we would like to have a better idea of our package design for our meeting 9.00am friday 12th august. MELBOURNE AUSTRALIA TIME!

dear norah,

we have already guaranteed $260.00. 

we expect to spend about $1,000-1,500 for this design project by the time we have accepted someone from the contest.

things that still need to be completed in 4 flavours...... and we will pay for! 
1. barcode
2. text
3. US nutritional panel
4. how to wrap instructions
5. ingredient lists
6. etc.
It's not about the money, money, money,
We don't need your money, money, money.
We just wanna make the world dance,
Forget about the paper moon.
Ain't about the (ha!) cha-ching cha-ching.
Ain't about the (yeah!) ba-bling ba-bling,
Wanna make the world dance,

Read more: http://artists.tunecorner.com/rosa-k-lyrics-paper-moon-feat-lu-t-xk52mrw#ixzz9R2KtPq0b 
TuneCorner - Your favorite Music Community 

desmond

Reason: only 5 designers (16 designs) have submitted work for assessment out of 37,000! I will award contest at the end of the extended 7 days desmond

Reason: because I can and the entries received to date are un satisfactory! desmond

Target Market(s)

our competitors in australia. see there packs in the links below

http://www.valleyloaf.com.au
http://www.pelicor.com.au/wv_softwraps.aspx
http://www.tqgfoods.com.au/nuvora2/index.php?option=com_zoo&view=item&Itemid=204

Industry/Entity Type

It Company

Requirements
Must have

• i FORGOT, THE PRODUCT IS DISPLAYED IN 2 WAYS

1. ABOVE THE ZIP LOCK CLOSE TO THE TOP 2 CORNERS ARE HANGING HOLES. THE PRODUCT SWINGS FROM 2 HOOKS IN A SUPER MARKET

2. THE PRODUCT IS STACKED. ONE ON TOP OF THE OTHER.

IN A SHELF
Nice to have
• HEALTHY, GREEN COLOURS, BROWNS, CREAMS, SOFT FONTS, LOGO OR SYMBOL? i DO NOT REALLY KNOW!
Should not have
• BRIGHT COLOURS! SCREAMING HEADLINES!

KEEP IN MIND THE SQUARE SHAPE PRODUCT AND THE PRODUCT COLOUR WILL BE SEEN THROUGH THE CLEAR PACK

```html
<!DOCTYPE html>
<html lang="en">
<head>
<meta charset="utf-8">
<title>Tidy Fold – Mediterranean Flat Bread Packs</title>
<link href="https://fonts.googleapis.com/css2?family=Kalam:wght@400&family=Open+Sans:wght@400;600&display=swap" rel="stylesheet">
<style>
  :root {
    --bg: #ffffff;
    --bag-light: #f7f7f7;
    --bag-shade: #e4e4e4;
    --seal: #d6d6d6;
    --label-black: #111111;
    --brand-cream: #f3dc9c;
    --text-light: #f2f2f2;
    --gold-rule: #c9a227;
    --badge-red: #d4221b;
    --corn: #df2a1f;
    --corn-band: #ef6b5f;
    --corn-art: #f15a45;
    --wholmeal: #f3a41f;
    --wholmeal-band: #e0703b;
    --wholmeal-edge: #b84f24;
    --wholmeal-art: #f6b84a;
    --white: #2fa9de;
    --white-band: #3b49a6;
    --white-art: #5cbde6;
    --small-print: #9a9a9a;
  }
  * { box-sizing: border-box; margin: 0; padding: 0; }
  html, body { width: 1200px; height: 721px; overflow: hidden; background: var(--bg); }
  .canvas {
    position: relative; width: 1200px; height: 721px;
    display: flex; justify-content: center; align-items: center; gap: 70px;
  }
  .pack {
    position: relative; width: 310px; height: 500px;
    background: linear-gradient(90deg, var(--bag-shade) 0%, var(--bag-light) 18%, var(--bag-light) 82%, var(--bag-shade) 100%);
    border-radius: 10px;
    box-shadow: 0 10px 24px rgba(0,0,0,0.12);
  }
  .seal {
    position: absolute; left: 0; right: 0; height: 34px;
    background: repeating-linear-gradient(90deg, var(--seal) 0 2px, var(--bag-light) 2px 6px);
  }
  .seal--top { top: 0; border-radius: 10px 10px 0 0; }
  .seal--bottom { bottom: 0; border-radius: 0 0 10px 10px; }
  .label {
    position: absolute; top: 34px; bottom: 34px; left: 70px; width: 170px;
    background: var(--label-black);
    display: flex; flex-direction: column; align-items: center;
    font-family: 'Open Sans', sans-serif; color: var(--text-light);
  }
  .brand-name {
    margin-top: 30px;
    font-family: 'Open Sans', sans-serif; font-weight: 600; font-size: 18px;
    line-height: 1.2; color: var(--brand-cream); letter-spacing: 0.5px;
  }
  .descriptor { margin-top: 6px; font-size: 10px; line-height: 1.2; text-align: center; width: 96px; }
  .flavour-disc {
    position: absolute; top: 118px; left: -48px; width: 266px; height: 186px;
    border-radius: 50%; border: 4px solid var(--label-black);
    display: flex; align-items: center; justify-content: center;
  }
  .flavour-art {
    position: absolute; left: 74px; top: 32px; width: 118px; height: 122px;
    border-radius: 40% 40% 45% 45%; opacity: 0.75;
  }
  .flavour-band {
    position: relative; width: 150px; height: 44px; border-radius: 8px;
    display: flex; align-items: center; justify-content: center;
    font-family: 'Kalam', cursive; font-size: 26px; color: var(--text-light);
  }
  .pack--corn .flavour-disc { background: var(--corn); }
  .pack--corn .flavour-band { background: var(--corn-band); }
  .pack--corn .flavour-art { background: var(--corn-art); }
  .pack--wholmeal .flavour-disc { background: var(--wholmeal); }
  .pack--wholmeal .flavour-band { background: var(--wholmeal-band); border: 2px solid var(--wholmeal-edge); }
  .pack--wholmeal .flavour-art { background: var(--wholmeal-art); }
  .pack--white .flavour-disc { background: var(--white); }
  .pack--white .flavour-band { background: var(--white-band); }
  .pack--white .flavour-art { background: var(--white-art); }
  .accreditation {
    position: absolute; top: 316px; width: 100%; text-align: center;
    font-size: 14px; line-height: 1.3;
  }
  .accreditation::after {
    content: ""; display: block; width: 130px; height: 2px; margin: 4px auto 0; background: var(--gold-rule);
  }
  .count-badge { position: absolute; top: 350px; left: 55px; width: 60px; height: 46px; }
  .small-print {
    position: absolute; bottom: 12px; width: 100%; text-align: center;
    font-size: 7px; line-height: 1.4; color: var(--small-print);
  }
</style>
</head>
<body>
<main class="canvas">

  <article class="pack pack--corn">
    <div class="seal seal--top"></div>
    <section class="label">
      <p class="brand-name">Tidy Fold</p>
      <p class="descriptor">Mediterranean Flat Bread</p>
      <div class="flavour-disc">
        <div class="flavour-art" role="img" aria-label="Line sketch of wheat stalks and flat bread sheets"></div>
        <div class="flavour-band">Corn</div>
      </div>
      <p class="accreditation">Kosher and Halal</p>
      <svg class="count-badge" viewBox="0 0 60 46" role="img" aria-label="8 pieces">
        <path d="M0 0 H60 V32 L30 46 L0 32 Z" fill="var(--badge-red)"/>
        <text x="30" y="18" text-anchor="middle" font-family="Open Sans, sans-serif" font-size="14" fill="#fff">8</text>
        <text x="30" y="29" text-anchor="middle" font-family="Open Sans, sans-serif" font-size="8" fill="#fff">Pieces</text>
      </svg>
      <p class="small-print">Made in Melbourne Australia<br>Net weight 250g</p>
    </section>
    <div class="seal seal--bottom"></div>
  </article>

  <article class="pack pack--wholmeal">
    <div class="seal seal--top"></div>
    <section class="label">
      <p class="brand-name">Tidy Fold</p>
      <p class="descriptor">Mediterranean Flat Bread</p>
      <div class="flavour-disc">
        <div class="flavour-art" role="img" aria-label="Line sketch of wheat stalks and flat bread sheets"></div>
        <div class="flavour-band">Wholmeal</div>
      </div>
      <p class="accreditation">Kosher and Halal</p>
      <svg class="count-badge" viewBox="0 0 60 46" role="img" aria-label="8 pieces">
        <path d="M0 0 H60 V32 L30 46 L0 32 Z" fill="var(--badge-red)"/>
        <text x="30" y="18" text-anchor="middle" font-family="Open Sans, sans-serif" font-size="14" fill="#fff">8</text>
        <text x="30" y="29" text-anchor="middle" font-family="Open Sans, sans-serif" font-size="8" fill="#fff">Pieces</text>
      </svg>
      <p class="small-print">Made in Melbourne Australia<br>Net weight 250g</p>
    </section>
    <div class="seal seal--bottom"></div>
  </article>

  <article class="pack pack--white">
    <div class="seal seal--top"></div>
    <section class="label">
      <p class="brand-name">Tidy Fold</p>
      <p class="descriptor">Mediterranean Flat Bread</p>
      <div class="flavour-disc">
        <div class="flavour-art" role="img" aria-label="Line sketch of wheat stalks and flat bread sheets"></div>
        <div class="flavour-band">White</div>
      </div>
      <p class="accreditation">Kosher and Halal</p>
      <svg class="count-badge" viewBox="0 0 60 46" role="img" aria-label="8 pieces">
        <path d="M0 0 H60 V32 L30 46 L0 32 Z" fill="var(--badge-red)"/>
        <text x="30" y="18" text-anchor="middle" font-family="Open Sans, sans-serif" font-size="14" fill="#fff">8</text>
        <text x="30" y="29" text-anchor="middle" font-family="Open Sans, sans-serif" font-size="8" fill="#fff">Pieces</text>
      </svg>
      <p class="small-print">Made in Melbourne Australia<br>Net weight 250g</p>
    </section>
    <div class="seal seal--bottom"></div>
  </article>

</main>
</body>
</html>
```